New, High-Tech Website for Venture Z - A Product Development Company

Venture Z is located in Silicon Valley, CA. We help companies build products from start to finish and everywhere in between. We build teams with top talent based on our customer's needs. We need a BRAND NEW website that looks innovative, fresh, new & modern. We want our website to impress companies that will hire us, as well as developers, designers, product people, etc.

The design is very important!

Target Market(s)

Small companies, entrepreneurs, anyone who needs help building a product or finding top talent

Industry/Entity Type

Tech

Coding

Coded - Design and coding required

Font styles to use
Sans Serif

Requirements
Must have
• Our logo (attached) and colors that look good with the logo.

**UPDATE - Site should be fully coded for WordPress and be MOBILE FRIENDLY. (Responsive Designs)
Nice to have
• We would love to see your ideas and if you have any other cool ideas to make our site POP and look attractive.

Please also let us know the following when you submit your design (in the notes section)!

1) Are we able to use any illustrations or images you provided legally? Would we need to pay any additional fees for images or illustrations?  If so, how much per picture/illustration?

2) If we choose your design, do your services include deploying the design to our Wordpress site?  Or, do you charge extra for this and how much?

3) If we choose your design, will this include any other page designs?  If so, how many?

4) If we choose your design, how much will you charge to design and implement other pages for us (like our contact us page, careers page, site map page, etc.) so our website looks cohesive?

5) What is your turnaround time for further page designs and implementations to the site?

6) Can you design AND implement surveys and/or custom questionnaires? What is the cost?
Should not have
• Nothing too "corporate" looking. For example, no images with men in suits around a large conference room because this doesn't represent who we are. We are more looking for images of people working - small startup company style.

Really cool, high tech illustrations are good too.

```html
<!DOCTYPE html>
<html lang="en">
<head>
<meta charset="utf-8">
<title>Venture Z — Product Development</title>
<link href="https://fonts.googleapis.com/css2?family=Montserrat:wght@400;500;600;700&display=swap" rel="stylesheet">
<style>
:root{
  --teal:#2bbfb0;
  --cyan:#2ac3e8;
  --navy:#2f3b55;
  --ink:#2e3a4f;
  --body:#5b6472;
  --soft:#f2f4f7;
  --line:#e3e7ec;
  --white:#ffffff;
  --footer-text:#c8cfdb;
  --grad:linear-gradient(90deg,var(--teal),var(--cyan));
}
*{box-sizing:border-box;margin:0;padding:0}
html,body{width:1200px;height:4612px;overflow:hidden}
body{position:relative;font-family:'Montserrat',sans-serif;color:var(--ink);background:var(--white)}
.abs{position:absolute}
a{color:inherit;text-decoration:none}

.btn{position:absolute;display:flex;align-items:center;justify-content:center;border-radius:40px;font-size:11.5px;font-weight:600;color:var(--ink);border:2px solid var(--teal);background:var(--white)}
.btn.solid{background:var(--grad);border:none;color:var(--white)}

.site-header{position:absolute;left:0;top:0;width:1200px;height:95px;background:var(--white);z-index:5}
.brand{position:absolute;display:flex;align-items:center;gap:8px;font-weight:700;color:var(--teal)}
.brand .dot{width:20px;height:20px;border-radius:50%;background:var(--teal)}
.nav a{position:absolute;top:38px;font-size:12px;font-weight:500;color:var(--ink)}
.nav a.active{color:var(--teal)}

.hero-photo{position:absolute;left:0;top:95px;width:1200px;height:640px;background:linear-gradient(120deg,#4b5a74 0%,#6c7c92 40%,#8b98aa 70%,#5d6d86 100%)}
.hero-shade{position:absolute;left:0;top:95px;width:1200px;height:640px;background:linear-gradient(90deg,rgba(47,59,85,.55),rgba(47,59,85,.05))}
.hero-title{left:88px;top:278px;font-size:48px;font-weight:500;color:var(--white);letter-spacing:-.5px}
.hero-sub{left:88px;top:350px;font-size:24px;line-height:30px;color:var(--white);font-weight:400}
.hero-sub b{font-weight:600}

.emblem{position:absolute;width:80px;height:80px;border-radius:50%;background:var(--grad);border:6px solid var(--white);box-shadow:0 4px 14px rgba(0,0,0,.12)}

.center{position:absolute;left:0;width:1200px;text-align:center}
.h2{font-size:39px;font-weight:400;color:var(--ink)}
.h2.teal{color:var(--teal)}
.intro-text{font-size:12.5px;line-height:19.5px;color:var(--body)}
.divider-shadow{position:absolute;left:0;top:1080px;width:1200px;height:14px;background:linear-gradient(var(--soft),rgba(242,244,247,0))}

.photo{position:absolute;border-radius:0 36px 36px 0}
.accent-v,.accent-h{position:absolute;background:var(--teal)}
.accent-h{background:var(--grad)}
.feature-title{position:absolute;font-size:31px;font-weight:500;color:var(--ink)}
.checklist{position:absolute;list-style:none}
.checklist li{position:absolute;left:0;white-space:nowrap;font-size:13.5px;line-height:19px;color:var(--body);padding-left:28px}
.checklist li svg{position:absolute;left:0;top:2px}

.soft-band{position:absolute;left:0;top:2722px;width:1200px;height:1000px;background:var(--soft)}
.hub{position:absolute;left:450px;top:2927px;width:300px;height:300px;border-radius:50%;background:var(--navy)}
.hub-name{position:absolute;left:450px;top:3134px;width:300px;text-align:center;color:var(--white);font-size:27px;font-weight:700}
.node{position:absolute;width:84px;height:84px;border-radius:50%;background:var(--white);border:6px solid #dcf3f1;display:flex;align-items:center;justify-content:center}
.node.on{background:var(--grad);border-color:#c4eef2}
.role{position:absolute;font-size:17px;font-weight:500;color:var(--ink);white-space:nowrap}
.role.right{text-align:right}

.service{position:absolute;top:3659px;width:256px;height:303px;text-align:center}
.service.featured{background:linear-gradient(135deg,var(--teal),var(--cyan))}
.service h3{position:absolute;left:0;top:116px;width:100%;font-size:17px;font-weight:600;color:var(--ink)}
.service p{position:absolute;left:26px;top:152px;width:204px;font-size:11px;line-height:18px;color:var(--body)}
.service.featured h3,.service.featured p{color:var(--white)}
.service .icon{position:absolute;left:100px;top:44px}
.service .btn{left:63px;top:236px;width:129px;height:34px}
.service.featured .btn{border-color:var(--white);color:var(--teal)}
.col-line{position:absolute;top:3665px;width:1px;height:290px;background:var(--line)}

.footer{position:absolute;left:0;top:4070px;width:1200px;height:542px;background:var(--navy)}
.foot-phone{left:88px;top:4362px;font-size:25px;color:var(--white);font-weight:400}
.foot-mail{left:88px;top:4396px;font-size:13px;color:var(--footer-text)}
.social{position:absolute;top:4440px;width:40px;height:40px;border-radius:50%;background:var(--white)}
.social.on{background:var(--teal);border:3px solid var(--white)}
.foot-h{position:absolute;top:4280px;font-size:18px;font-weight:600;color:var(--white)}
.foot-link{position:absolute;font-size:12px;color:var(--footer-text)}
.field{position:absolute;left:792px;top:4327px;width:320px;height:33px;border-radius:20px;background:#45516c;color:#aab3c2;font-size:11.5px;padding:9px 20px}
.copy{left:88px;top:4531px;font-size:11.5px;color:var(--footer-text)}
.copy span{color:var(--teal)}
</style>
</head>
<body>

<header class="site-header">
  <div class="brand" style="left:88px;top:34px;font-size:18px"><span class="dot"></span>Venture Z</div>
  <nav class="nav">
    <a class="active" style="left:313px">Home</a>
    <a style="left:387px">Services</a>
    <a style="left:476px">About</a>
    <a style="left:550px">Testimonials &amp; Press</a>
    <a style="left:707px">Careers</a>
    <a style="left:790px">Blog</a>
  </nav>
  <a class="btn solid" style="left:849px;top:30px;width:127px;height:36px">Apply Now</a>
  <a class="btn" style="left:998px;top:30px;width:114px;height:36px">Get in Touch</a>
</header>

<div class="hero-photo" role="img" aria-label="Team working together around a table covered with sketches, laptops and notes"></div>
<div class="hero-shade"></div>
<h1 class="abs hero-title">Welcome to Venture Z</h1>
<p class="abs hero-sub">The #1 leader in <b>product development services,</b><br>based in Silicon Valley, CA</p>
<a class="btn solid" style="left:88px;top:435px;width:129px;height:34px">Contact Us</a>

<svg class="abs" style="left:0;top:620px" width="1200" height="120" viewBox="0 0 1200 120">
  <path d="M0 115 Q600 -20 1200 115 L1200 120 L0 120 Z" fill="#ffffff"/>
  <path d="M60 70 Q600 18 1140 70" fill="none" stroke="#2ac3e8" stroke-width="6" stroke-linecap="round"/>
</svg>
<div class="emblem" style="left:560px;top:626px"></div>

<h2 class="center h2" style="top:775px">Need help building a product?</h2>
<h2 class="center h2 teal" style="top:821px">We are here for you!</h2>
<p class="center intro-text" style="top:874px">Venture Z works with companies of all sizes to design, build &amp; launch exceptional products from start to finish<br>(and anywhere in between.) We take ideas from concept to launch, or can step into organizations that are experiencing<br>product troubles and advise on how to clear roadblocks.</p>
<a class="btn" style="left:512px;top:965px;width:176px;height:35px">Explore Our Services</a>
<div class="divider-shadow"></div>

<div class="accent-v" style="left:88px;top:1379px;width:23px;height:262px"></div>
<div class="accent-h" style="left:88px;top:1617px;width:184px;height:24px"></div>
<div class="photo" style="left:111px;top:1161px;width:376px;height:456px;background:linear-gradient(135deg,#c9d4e2,#8ea2bb 55%,#5d6f8a)" role="img" aria-label="Two colleagues shaking hands across a meeting table"></div>
<h2 class="feature-title" style="left:616px;top:1197px">We love to work with</h2>
<ul class="checklist" style="left:616px;top:0">
  <li style="top:1254px"><svg width="14" height="14" viewBox="0 0 14 14"><circle cx="7" cy="7" r="6" fill="none" stroke="#2bbfb0" stroke-width="1.4"/><path d="M4.3 7.2l1.9 1.8 3.5-3.6" fill="none" stroke="#2bbfb0" stroke-width="1.4"/></svg>Entrepreneurs with an idea who wants to build a beta product<br>or business</li>
  <li style="top:1311px"><svg width="14" height="14" viewBox="0 0 14 14"><circle cx="7" cy="7" r="6" fill="none" stroke="#2bbfb0" stroke-width="1.4"/><path d="M4.3 7.2l1.9 1.8 3.5-3.6" fill="none" stroke="#2bbfb0" stroke-width="1.4"/></svg>Start Up Companies who need a product built quickly and cost<br>effectively</li>
  <li style="top:1368px"><svg width="14" height="14" viewBox="0 0 14 14"><circle cx="7" cy="7" r="6" fill="none" stroke="#2bbfb0" stroke-width="1.4"/><path d="M4.3 7.2l1.9 1.8 3.5-3.6" fill="none" stroke="#2bbfb0" stroke-width="1.4"/></svg>Small or medium sized, more established companies that are<br>having issues shipping product</li>
  <li style="top:1426px"><svg width="14" height="14" viewBox="0 0 14 14"><circle cx="7" cy="7" r="6" fill="none" stroke="#2bbfb0" stroke-width="1.4"/><path d="M4.3 7.2l1.9 1.8 3.5-3.6" fill="none" stroke="#2bbfb0" stroke-width="1.4"/></svg>Larger sized companies that need Product Management<br>consulting</li>
  <li style="top:1483px"><svg width="14" height="14" viewBox="0 0 14 14"><circle cx="7" cy="7" r="6" fill="none" stroke="#2bbfb0" stroke-width="1.4"/><path d="M4.3 7.2l1.9 1.8 3.5-3.6" fill="none" stroke="#2bbfb0" stroke-width="1.4"/></svg>Companies of all sizes that need great talent, quickly.</li>
</ul>
<a class="btn" style="left:616px;top:1538px;width:127px;height:35px">Contact Us</a>

<h2 class="feature-title" style="left:88px;top:1716px">Things that excite us</h2>
<ul class="checklist" style="left:88px;top:0">
  <li style="top:1773px"><svg width="14" height="14" viewBox="0 0 14 14"><circle cx="7" cy="7" r="6" fill="none" stroke="#2bbfb0" stroke-width="1.4"/><path d="M4.3 7.2l1.9 1.8 3.5-3.6" fill="none" stroke="#2bbfb0" stroke-width="1.4"/></svg>Innovation</li>
  <li style="top:1812px"><svg width="14" height="14" viewBox="0 0 14 14"><circle cx="7" cy="7" r="6" fill="none" stroke="#2bbfb0" stroke-width="1.4"/><path d="M4.3 7.2l1.9 1.8 3.5-3.6" fill="none" stroke="#2bbfb0" stroke-width="1.4"/></svg>New design &amp; technology</li>
  <li style="top:1850px"><svg width="14" height="14" viewBox="0 0 14 14"><circle cx="7" cy="7" r="6" fill="none" stroke="#2bbfb0" stroke-width="1.4"/><path d="M4.3 7.2l1.9 1.8 3.5-3.6" fill="none" stroke="#2bbfb0" stroke-width="1.4"/></svg>Clear Roadmaps</li>
  <li style="top:1889px"><svg width="14" height="14" viewBox="0 0 14 14"><circle cx="7" cy="7" r="6" fill="none" stroke="#2bbfb0" stroke-width="1.4"/><path d="M4.3 7.2l1.9 1.8 3.5-3.6" fill="none" stroke="#2bbfb0" stroke-width="1.4"/></svg>Product Releases</li>
  <li style="top:1927px"><svg width="14" height="14" viewBox="0 0 14 14"><circle cx="7" cy="7" r="6" fill="none" stroke="#2bbfb0" stroke-width="1.4"/><path d="M4.3 7.2l1.9 1.8 3.5-3.6" fill="none" stroke="#2bbfb0" stroke-width="1.4"/></svg>Brining ideas to life</li>
  <li style="top:1965px"><svg width="14" height="14" viewBox="0 0 14 14"><circle cx="7" cy="7" r="6" fill="none" stroke="#2bbfb0" stroke-width="1.4"/><path d="M4.3 7.2l1.9 1.8 3.5-3.6" fill="none" stroke="#2bbfb0" stroke-width="1.4"/></svg>Solving Busines Challenges</li>
  <li style="top:2004px"><svg width="14" height="14" viewBox="0 0 14 14"><circle cx="7" cy="7" r="6" fill="none" stroke="#2bbfb0" stroke-width="1.4"/><path d="M4.3 7.2l1.9 1.8 3.5-3.6" fill="none" stroke="#2bbfb0" stroke-width="1.4"/></svg>Happy Clients</li>
</ul>
<a class="btn" style="left:88px;top:2060px;width:129px;height:34px">Contact Us</a>
<div class="accent-v" style="left:713px;top:1898px;width:23px;height:264px"></div>
<div class="accent-h" style="left:713px;top:2137px;width:183px;height:25px"></div>
<div class="photo" style="left:736px;top:1682px;width:376px;height:455px;background:linear-gradient(135deg,#6e6a63,#9a958c 45%,#d9d6c4 60%,#5b5851)" role="img" aria-label="Hands assembling paper squares into a yellow light bulb on a wooden table"></div>

<div class="accent-v" style="left:88px;top:2418px;width:23px;height:263px"></div>
<div class="accent-h" style="left:88px;top:2658px;width:184px;height:23px"></div>
<div class="photo" style="left:111px;top:2201px;width:376px;height:457px;background:linear-gradient(135deg,#8a7b8a,#b79a92 50%,#6c6577)" role="img" aria-label="Circle of joined fists from a team"></div>
<h2 class="feature-title" style="left:616px;top:2255px">Things that we promise</h2>
<ul class="checklist" style="left:616px;top:0">
  <li style="top:2314px"><svg width="14" height="14" viewBox="0 0 14 14"><circle cx="7" cy="7" r="6" fill="none" stroke="#2bbfb0" stroke-width="1.4"/><path d="M4.3 7.2l1.9 1.8 3.5-3.6" fill="none" stroke="#2bbfb0" stroke-width="1.4"/></svg>Experience, Passion &amp; Impact</li>
  <li style="top:2352px"><svg width="14" height="14" viewBox="0 0 14 14"><circle cx="7" cy="7" r="6" fill="none" stroke="#2bbfb0" stroke-width="1.4"/><path d="M4.3 7.2l1.9 1.8 3.5-3.6" fill="none" stroke="#2bbfb0" stroke-width="1.4"/></svg>Focused strategies</li>
  <li style="top:2391px"><svg width="14" height="14" viewBox="0 0 14 14"><circle cx="7" cy="7" r="6" fill="none" stroke="#2bbfb0" stroke-width="1.4"/><path d="M4.3 7.2l1.9 1.8 3.5-3.6" fill="none" stroke="#2bbfb0" stroke-width="1.4"/></svg>Great People &amp; High Functioning Teams</li>
  <li style="top:2429px"><svg width="14" height="14" viewBox="0 0 14 14"><circle cx="7" cy="7" r="6" fill="none" stroke="#2bbfb0" stroke-width="1.4"/><path d="M4.3 7.2l1.9 1.8 3.5-3.6" fill="none" stroke="#2bbfb0" stroke-width="1.4"/></svg>Integrity, Reliability &amp; Security</li>
  <li style="top:2468px"><svg width="14" height="14" viewBox="0 0 14 14"><circle cx="7" cy="7" r="6" fill="none" stroke="#2bbfb0" stroke-width="1.4"/><path d="M4.3 7.2l1.9 1.8 3.5-3.6" fill="none" stroke="#2bbfb0" stroke-width="1.4"/></svg>Data driven &amp; Design centric results</li>
  <li style="top:2506px"><svg width="14" height="14" viewBox="0 0 14 14"><circle cx="7" cy="7" r="6" fill="none" stroke="#2bbfb0" stroke-width="1.4"/><path d="M4.3 7.2l1.9 1.8 3.5-3.6" fill="none" stroke="#2bbfb0" stroke-width="1.4"/></svg>Top customer service for our clients</li>
</ul>
<a class="btn" style="left:616px;top:2561px;width:127px;height:34px">Contact Us</a>

<div class="soft-band"></div>
<svg class="abs" style="left:0;top:2722px" width="1200" height="140" viewBox="0 0 1200 140">
  <path d="M0 0 L1200 0 L1200 60 Q600 150 0 60 Z" fill="#ffffff"/>
  <path d="M188 86 Q600 150 1003 86" fill="none" stroke="#2ac3e8" stroke-width="6" stroke-linecap="round"/>
</svg>
<div class="hub"></div>
<div class="hub-name">Venture Z</div>

<div class="node" style="left:468px;top:2915px"><svg width="34" height="34" viewBox="0 0 34 34" fill="none" stroke="#2bbfb0" stroke-width="1.8"><rect x="4" y="5" width="26" height="24" rx="2"/><path d="M4 10h26"/><circle cx="17" cy="20" r="5"/></svg></div>
<div class="node on" style="left:646px;top:2915px"><svg width="34" height="34" viewBox="0 0 34 34" fill="none" stroke="#fff" stroke-width="1.8"><path d="M17 6l7 12-7 10-7-10z"/><path d="M4 10h26"/><circle cx="17" cy="18" r="2"/></svg></div>
<div class="node" style="left:397px;top:3049px"><svg width="34" height="34" viewBox="0 0 34 34" fill="none" stroke="#2bbfb0" stroke-width="1.8"><rect x="4" y="5" width="22" height="20" rx="2"/><circle cx="18" cy="18" r="6"/><path d="M22 22l8 8"/></svg></div>
<div class="node" style="left:714px;top:3049px"><svg width="34" height="34" viewBox="0 0 34 34" fill="none" stroke="#2bbfb0" stroke-width="1.8"><rect x="4" y="6" width="26" height="18" rx="2"/><path d="M12 29h10M17 24v5M9 12l4 3-4 3M16 18h6"/></svg></div>
<div class="node" style="left:468px;top:3185px"><svg width="34" height="34" viewBox="0 0 34 34" fill="none" stroke="#2bbfb0" stroke-width="1.8"><circle cx="17" cy="17" r="11"/><circle cx="17" cy="17" r="5"/><path d="M17 3v4M17 27v4M3 17h4M27 17h4"/></svg></div>
<div class="node" style="left:646px;top:3185px"><svg width="34" height="34" viewBox="0 0 34 34" fill="none" stroke="#2bbfb0" stroke-width="1.8"><rect x="4" y="4" width="20" height="26" rx="2"/><path d="M9 11h10M9 17h10M9 23h6"/><path d="M22 22l3 3 6-7"/></svg></div>

<div class="role right" style="left:233px;top:2944px;width:200px">Finalized Product</div>
<div class="role" style="left:765px;top:2945px">Designers</div>
<div class="role right" style="left:164px;top:3080px;width:200px">Researchers</div>
<div class="role" style="left:831px;top:3080px">Developers</div>
<div class="role right" style="left:233px;top:3216px;width:200px">Product Managers</div>
<div class="role" style="left:765px;top:3216px">QA</div>
<a class="btn" style="left:537px;top:3317px;width:126px;height:34px;background:transparent">Get in Touch</a>

<svg class="abs" style="left:0;top:3440px" width="1200" height="110" viewBox="0 0 1200 110">
  <path d="M0 80 Q600 -10 1200 80 L1200 110 L0 110 Z" fill="#ffffff"/>
  <path d="M120 72 Q600 -4 1080 72" fill="none" stroke="#2ac3e8" stroke-width="6" stroke-linecap="round"/>
</svg>
<div class="abs" style="left:0;top:3545px;width:1200px;height:525px;background:#fff"></div>
<h2 class="center h2" style="top:3535px">Our Services</h2>
<h2 class="center h2 teal" style="top:3580px">We build teams that deliver!</h2>

<div class="service" style="left:88px">
  <svg class="icon" width="56" height="56" viewBox="0 0 56 56" fill="none" stroke="#2bbfb0" stroke-width="2"><rect x="10" y="6" width="34" height="44" rx="3"/><path d="M17 16h20M17 24h12"/><circle cx="30" cy="36" r="7"/><path d="M35 41l7 7"/></svg>
  <h3>Research</h3>
  <p>It is a long established fact that a reader will be distracted by the readable content of a page.</p>
  <a class="btn">Get in Touch</a>
</div>
<div class="service featured" style="left:344px">
  <svg class="icon" width="56" height="56" viewBox="0 0 56 56" fill="none" stroke="#fff" stroke-width="2"><path d="M8 48h40L8 8z"/><path d="M16 40h12L16 28z"/><path d="M30 30l16-16 4 4-16 16-6 2z"/></svg>
  <h3>Design</h3>
  <p>It is a long established fact that a reader will be distracted by the readable content of a page.</p>
  <a class="btn">Apply Here</a>
</div>
<div class="service" style="left:600px">
  <svg class="icon" width="56" height="56" viewBox="0 0 56 56" fill="none" stroke="#2bbfb0" stroke-width="2"><path d="M16 22a12 12 0 0124 0z"/><path d="M12 22h32"/><path d="M20 26a8 8 0 0016 0"/><path d="M10 50c2-10 10-14 18-14s16 4 18 14z"/></svg>
  <h3>Engineers</h3>
  <p>It is a long established fact that a reader will be distracted by the readable content of a page.</p>
  <a class="btn">Our Approach</a>
</div>
<div class="service" style="left:856px">
  <svg class="icon" width="56" height="56" viewBox="0 0 56 56" fill="none" stroke="#2bbfb0" stroke-width="2"><circle cx="28" cy="26" r="12"/><circle cx="28" cy="26" r="5"/><path d="M28 8v5M28 39v5M10 26h5M41 26h5M15 13l4 4M37 35l4 4M41 13l-4 4M15 39l4-4"/><path d="M22 50h12"/></svg>
  <h3>Product Managers</h3>
  <p>It is a long established fact that a reader will be distracted by the readable content of a page.</p>
  <a class="btn">Why Us</a>
</div>
<div class="col-line" style="left:856px"></div>
<a class="btn" style="left:519px;top:4005px;width:160px;height:34px">View All Services</a>

<footer class="footer"></footer>
<svg class="abs" style="left:0;top:4064px" width="1200" height="120" viewBox="0 0 1200 120">
  <path d="M0 0 L1200 0 L1200 20 Q600 150 0 20 Z" fill="#ffffff"/>
  <path d="M80 70 Q600 130 1120 70" fill="none" stroke="#2ac3e8" stroke-width="6" stroke-linecap="round"/>
</svg>
<div class="emblem" style="left:560px;top:4119px"></div>

<div class="brand" style="left:88px;top:4300px;font-size:16px"><span class="dot"></span>Venture Z</div>
<p class="abs foot-phone">Call. 800.555.0142</p>
<p class="abs foot-mail">e. hello@venturez.co</p>
<span class="social" style="left:87px"></span>
<span class="social on" style="left:134px;top:4437px;width:46px;height:46px"></span>
<span class="social" style="left:184px"></span>

<h4 class="foot-h" style="left:440px">Quick links</h4>
<a class="foot-link" style="left:440px;top:4333px">Freelancers</a>
<a class="foot-link" style="left:440px;top:4356px">Companies</a>
<a class="foot-link" style="left:440px;top:4380px">Services</a>
<a class="foot-link" style="left:440px;top:4404px">Our Approach</a>
<a class="foot-link" style="left:440px;top:4427px">Why Us</a>
<a class="foot-link" style="left:440px;top:4452px">FAQ</a>
<a class="foot-link" style="left:440px;top:4476px">Contact Us</a>
<a class="foot-link" style="left:584px;top:4333px">Privacy Policy</a>
<a class="foot-link" style="left:584px;top:4356px">Terms &amp; Conditions</a>
<a class="foot-link" style="left:584px;top:4380px">Security &amp; Compliance</a>

<h4 class="foot-h" style="left:792px">Subscribe to our blog</h4>
<div class="field">name@email.com</div>
<a class="btn solid" style="left:792px;top:4381px;width:112px;height:33px">Submit</a>

<p class="abs copy">© 2021 <span>Venture Z</span>. All Rights Reserved</p>

</body>
</html>
```